Tour agency for FIT and groups need a business card design

We need a business card design for a tour agency company that is based in Perth called" BRISK NO", we aim to provide customise, unique and seamless travel arrangement for FIT and groups. We serve both high profile businessperson, government authorities, business partners, executives and investors. The name card should be more professional looking.
Updates

Project Deadline Extended Reason: Have some changes that needed to make, director will be back to office on Monday, sorry for the inconvenience cause. Added Saturday, May 6, 2017

Target Market(s)

High profile businessperson, government authorities, business partners, executives and investors.

Industry/Entity Type

Tourism

Contact Information for Business Card

Brisk NO
Level 1, 214 Marlowe Avenue, Dunreath NO, 6120
www.briskno.com.au

Font styles to use
Serif

Colors

Designer to choose colors to be used in the design.

Requirements
Must have
• My project must have a company logo
Nice to have
• a more professional and solid yet friendly name card design. We may want to include chinese name in the name card as well. Edge of the card can be filled with gold and we think that transparent name cards are interesting.

```html
<!DOCTYPE html>
<html lang="en">
<head>
<meta charset="utf-8">
<title>Brisk NO – Business Card</title>
<link rel="stylesheet" href="https://fonts.googleapis.com/css2?family=Mulish:wght@300;400&display=swap">
<style>
  :root {
    --card-bg: #ffffff;
    --ink: #111111;
    --brand-blue: #29a3dc;
  }
  html, body {
    margin: 0;
    padding: 0;
    width: 1200px;
    height: 777px;
    overflow: hidden;
    background: var(--card-bg);
  }
  .card {
    position: relative;
    width: 1200px;
    height: 777px;
    background: var(--card-bg);
    font-family: "Mulish", sans-serif;
    font-weight: 300;
    color: var(--ink);
  }
  .card__line {
    position: absolute;
    left: 100px;
    margin: 0;
    line-height: 1;
    white-space: nowrap;
  }
  .card__name {
    top: 98px;
    font-size: 41px;
    font-weight: 400;
  }
  .card__role {
    top: 157px;
    font-size: 36px;
  }
  .card__company {
    top: 211px;
    font-size: 36px;
    color: var(--brand-blue);
    font-weight: 400;
  }
  .card__address {
    top: 265px;
    font-size: 36px;
  }
  .card__email {
    top: 369px;
    font-size: 36px;
  }
  .card__mobile {
    top: 415px;
    font-size: 36px;
  }
  .card__website {
    top: 606px;
    font-size: 38px;
    color: var(--brand-blue);
  }
  .card__brand {
    position: absolute;
    right: 120px;
    top: 570px;
    margin: 0;
    font-size: 84px;
    line-height: 1;
    font-weight: 400;
    color: var(--brand-blue);
  }
</style>
</head>
<body>
  <main class="card">
    <p class="card__line card__name">Your name here</p>
    <p class="card__line card__role">Job title</p>
    <p class="card__line card__company">Brisk NO</p>
    <p class="card__line card__address">Level 1, 214 Marlowe Avenue, Dunreath NO, 6120</p>
    <p class="card__line card__email">Email:</p>
    <p class="card__line card__mobile">Mobile:</p>
    <p class="card__line card__website">briskno.com.au</p>
    <p class="card__brand">Briskno</p>
  </main>
</body>
</html>
```